Home page design for a live auction website.

Hi, we are looking at finding a good design for an auction website, only home page .. We will not be selling anything online, so the website will only be a portal where visitors can check about our company, upcoming auctions, online catalogues etc.
See attached our logo. Please use the same red that you see on the logo in the designs that you provide.
The final design should communicate high-end auction website, as we will be selling expensive piece of arts and antiques.
We should have a main frame where images of arts will circulate, with description of the art piece. just like on http://paris.vellmarotte-quisande.com/
(but with a better design overall) and of course a menu with different tabs, like "about us", "previous sales" "next sales", "contact" , "how to buy", "meet our specialists".

Target Market(s)

High end segment, who can afford to pay up to 250'000 for a piece of art

Industry/Entity Type

Online

Number of Pages Required

1 page

Requirements
Must have
• a frame with images rotating, just like on http://paris.vellmarotte-quisande.com/ . but the rest of the design should be more refined.
• we should also have a strong call to action, "Free online estimation", click here, estimation delivered in 48 hours"
Nice to have
• Tremaux Auctions, the brand should be well visible

```html
<!DOCTYPE html>
<html lang="en">
<head>
<meta charset="utf-8">
<title>Tremaux Auctions</title>
<link href="https://fonts.googleapis.com/css2?family=Open+Sans:wght@400;600;700;800&display=swap" rel="stylesheet">
<style>
:root{
  --red:#c0171d;
  --red-dark:#9e1015;
  --ink:#2b2b2b;
  --text:#6f6f6f;
  --muted:#9a9a9a;
  --line:#e3e3e3;
  --dark:#2c2f33;
  --darker:#222427;
  --paper:#ffffff;
  --soft:#f4f4f4;
}
*{box-sizing:border-box;margin:0;padding:0}
html,body{width:1200px;height:2208px;overflow:hidden}
body{font-family:"Open Sans",Arial,sans-serif;color:var(--text);background:var(--paper);position:relative}
a{color:inherit;text-decoration:none}

.topbar{height:26px;background:var(--soft);border-bottom:1px solid var(--line);display:flex;justify-content:space-between;align-items:center;padding:0 60px;font-size:11px;color:var(--muted)}
.topbar .contacts{display:flex;gap:22px}
.topbar .contacts span{display:flex;align-items:center;gap:6px}

.header{height:62px;display:flex;align-items:center;justify-content:space-between;padding:0 60px}
.brand{display:flex;align-items:center;gap:10px;color:var(--red);font-weight:700;font-size:18px;letter-spacing:1px;text-transform:uppercase}
.brand .mark{width:14px;height:14px;background:var(--red)}
.nav{display:flex;align-items:center;gap:26px;font-size:11px;font-weight:700;color:var(--ink);text-transform:uppercase}
.nav .active{color:var(--red);border-bottom:2px solid var(--red);padding-bottom:4px}
.btn{display:inline-block;background:var(--red);color:#fff;font-weight:700;font-size:11px;text-transform:uppercase;padding:10px 18px;border-radius:3px}

.hero{position:relative;height:572px;background:radial-gradient(ellipse at 62% 35%,#d9cbb0 0,#8a7456 22%,#3a2e24 48%,#1a1512 80%);}
.hero .caption{position:absolute;left:100px;right:100px;top:462px;height:92px;background:var(--red);display:flex;align-items:center;padding:0 30px;gap:30px;color:#fff}
.caption h2{font-size:17px;font-weight:700;margin-bottom:6px}
.caption p{font-size:11px;line-height:1.5;opacity:.9}
.caption .btn{background:var(--red-dark);border:1px solid #fff;border-radius:20px;white-space:nowrap}
.arrow{position:absolute;width:36px;height:36px;display:flex;align-items:center;justify-content:center}
.hero .arrow{top:490px}

.intro{display:flex;gap:50px;padding:60px 80px 50px}
.welcome{flex:1}
.welcome small{display:block;font-size:16px;color:var(--ink)}
.welcome h1{font-size:28px;color:var(--red);font-weight:600;padding-bottom:10px;border-bottom:2px solid var(--red);display:inline-block;margin-bottom:22px}
.welcome p{font-size:12px;line-height:1.8;margin-bottom:18px}
.catalog{width:330px}
.catalog h3{font-size:18px;font-weight:600;color:var(--ink);margin-bottom:14px}
.cat-item{display:flex;gap:12px;padding:10px;background:var(--soft);margin-bottom:8px}
.cat-item .thumb{width:68px;height:68px;flex:none}
.cat-item p{font-size:11px;color:var(--red);line-height:1.5}
.cat-item span{font-size:10px;color:var(--muted)}

.upcoming{position:relative;height:560px;background:linear-gradient(#3a3d41,var(--dark));padding-top:36px}
.upcoming h2{text-align:center;color:#fff;font-size:24px;font-weight:600;margin-bottom:28px}
.auction-card{margin:0 80px;height:430px;background:#fff;display:flex}
.auction-card .photo{width:500px;flex:none;background:linear-gradient(120deg,#2a1a10,#6b3a1c 40%,#b5782e 60%,#3d2414)}
.auction-card .body{padding:40px 40px}
.auction-card .date{font-size:11px;color:var(--muted)}
.auction-card h3{font-size:18px;color:var(--ink);font-weight:600;line-height:1.5;margin:10px 0 16px}
.auction-card p{font-size:12px;line-height:1.8;margin-bottom:16px}
.btn-outline{display:inline-block;border:1px solid var(--ink);border-radius:20px;padding:8px 18px;font-size:10px;font-weight:700;color:var(--ink);text-transform:uppercase}
.upcoming .arrow{top:300px;background:rgba(255,255,255,.15);border-radius:50%}

.estimation{display:flex;align-items:center;gap:40px;padding:40px 70px;height:390px}
.estimation .chair{width:250px;height:260px;flex:none;background:radial-gradient(ellipse,#d8b56a 0,#a8803f 45%,#fff 72%)}
.cta{flex:1;height:260px;background:var(--red);color:#fff;text-align:center;display:flex;flex-direction:column;align-items:center;justify-content:center}
.cta .free{font-size:40px;font-weight:800;color:var(--ink);background:#fff;padding:0 30px;margin-bottom:10px}
.cta .big{font-size:48px;font-weight:800;line-height:1}
.cta .sub{font-size:24px;font-weight:700;margin:10px 0 18px}
.cta .go{background:#111;color:#fff;font-weight:700;font-size:18px;padding:10px 26px;text-transform:uppercase}

.footer{position:absolute;left:0;right:0;bottom:0;height:250px;background:var(--darker);color:#a7a7a7;display:flex;gap:60px;padding:40px 70px;font-size:11px;line-height:1.8}
.footer .brand{font-size:15px;margin-bottom:14px}
.footer h4{color:#fff;font-size:13px;margin-bottom:10px}
.links{display:grid;grid-template-columns:120px 140px;column-gap:20px}
.social{margin-left:auto;width:220px}
.social a{display:flex;align-items:center;gap:10px;color:#fff;padding:7px 12px;margin-bottom:6px;font-size:12px}
.social .sq{width:12px;height:12px;background:#fff}
</style>
</head>
<body>
<div class="topbar">
  <span>Welcome, Tremaux Auctions</span>
  <div class="contacts">
    <span><svg width="10" height="10" viewBox="0 0 10 10"><path d="M2 1l2 2-1 1a6 6 0 003 3l1-1 2 2-1.5 1.5C4 9 1 6 .5 2.5z" fill="#9a9a9a"/></svg>(555) 014 2290</span>
    <span><svg width="11" height="9" viewBox="0 0 11 9"><rect x=".5" y=".5" width="10" height="8" fill="none" stroke="#9a9a9a"/><path d="M.5.5l5 4 5-4" fill="none" stroke="#9a9a9a"/></svg>info@tremauxauctions.com</span>
  </div>
</div>

<header class="header">
  <div class="brand"><span class="mark"></span>Tremaux Auctions</div>
  <nav class="nav">
    <a class="active">Home</a><a>About Us</a><a>Previous Sales</a><a>Next Sales</a><a>Contact</a><a>Meet Our Specialists</a>
    <a class="btn">How to Buy</a>
  </nav>
</header>

<section class="hero" role="img" aria-label="Antique gold pocket watch photographed on a dark background">
  <svg class="arrow" style="left:60px" viewBox="0 0 36 36"><path d="M22 8l-10 10 10 10" stroke="#fff" stroke-width="3" fill="none"/></svg>
  <svg class="arrow" style="right:60px" viewBox="0 0 36 36"><path d="M14 8l10 10-10 10" stroke="#fff" stroke-width="3" fill="none"/></svg>
  <div class="caption">
    <div>
      <h2>Lorem ipsum dolor sit amet, consectetuer adipiscing elit, sed diam nonummy</h2>
      <p>Duis autem vel eum iriure dolor in hendrerit in vulputate velit esse molestie consequat, vel illum dolore eu feugiat nulla facilisis at vero eros et accumsan et iusto odio dignissim qui blandit praesent luptatum zzril delenit augue duis dolore te feugait nulla facilisi.</p>
    </div>
    <a class="btn">Learn More</a>
  </div>
</section>

<section class="intro">
  <div class="welcome">
    <small>Welcome to</small>
    <h1>Tremaux Auctions</h1>
    <p>Lorem ipsum dolor sit amet, consectetuer adipiscing elit, sed diam nonummy nibh euismod tincidunt ut laoreet dolore magna aliquam erat volutpat. Ut wisi enim ad minim veniam, quis nostrud exerci tation ullamcorper suscipit lobortis nisl ut aliquip ex ea commodo consequat.</p>
    <p>Duis autem vel eum iriure dolor in hendrerit in vulputate velit esse molestie consequat, vel illum dolore eu feugiat nulla facilisis at vero eros et accumsan et iusto odio dignissim qui blandit praesent luptatum zzril delenit augue duis dolore te feugait nulla facilisi. Nam liber tempor cum soluta nobis eleifend option congue nihil imperdiet doming id quod mazim placerat facer possim assum.</p>
  </div>
  <aside class="catalog">
    <h3>Online Catalog</h3>
    <div class="cat-item"><div class="thumb" role="img" aria-label="Religious painting in blue and gold" style="background:linear-gradient(135deg,#3f5f9a,#c9a85a)"></div><div><p>Duis autem vel eum iriure dolor in hendrerit in vulputate</p><span>Catalog</span></div></div>
    <div class="cat-item"><div class="thumb" role="img" aria-label="Landscape painting in green tones" style="background:linear-gradient(135deg,#4e6a3a,#a8b07a)"></div><div><p>Duis autem vel eum iriure dolor in hendrerit in vulputate</p><span>Catalog</span></div></div>
    <div class="cat-item"><div class="thumb" role="img" aria-label="Gilt framed still life painting" style="background:linear-gradient(135deg,#6b4a22,#d8b86a)"></div><div><p>Duis autem vel eum iriure dolor in hendrerit in vulputate</p><span>Catalog</span></div></div>
  </aside>
</section>

<section class="upcoming">
  <h2>Upcoming Auctions</h2>
  <svg class="arrow" style="left:20px" viewBox="0 0 36 36"><path d="M21 11l-7 7 7 7" stroke="#fff" stroke-width="3" fill="none"/></svg>
  <svg class="arrow" style="right:20px" viewBox="0 0 36 36"><path d="M15 11l7 7-7 7" stroke="#fff" stroke-width="3" fill="none"/></svg>
  <div class="auction-card">
    <div class="photo" role="img" aria-label="Ornate gilt bronze mantel clock on red velvet"></div>
    <div class="body">
      <div class="date">12 September 2015</div>
      <h3>Lorem ipsum dolor sit amet, consectetuer adipiscing elit, sed diam nonummy nibh euismod tincidunt ut laoreet dolore magna aliquam erat volutpat.</h3>
      <p>Duis autem vel eum iriure dolor in hendrerit in vulputate velit esse molestie consequat, vel illum dolore eu feugiat nulla facilisis.</p>
      <p>Duis autem vel eum iriure dolor in hendrerit in vulputate velit esse molestie consequat, vel illum dolore eu feugiat nulla facilisis at vero eros et accumsan et iusto odio dignissim qui blandit praesent luptatum.</p>
      <a class="btn-outline">Learn More</a>
    </div>
  </div>
</section>

<section class="estimation">
  <div class="chair" role="img" aria-label="Gilded antique armchair with upholstered seat"></div>
  <div class="cta">
    <div class="free">FREE</div>
    <div class="big">ONLINE ESTIMATION</div>
    <div class="sub">ESTIMATION DELIVERED IN 48 HOURS</div>
    <a class="go">Click Here</a>
  </div>
</section>

<footer class="footer">
  <div>
    <div class="brand"><span class="mark"></span>Tremaux Auctions</div>
    <div>© 2015 Tremaux Auctions</div>
  </div>
  <div>
    <h4>Get in Touch</h4>
    <div>14 Rue Lorem, Ipsum district<br>75000 Paris, France<br>(555) 014 2290<br>info@tremauxauctions.com</div>
  </div>
  <div>
    <h4>Quick Links</h4>
    <div class="links"><a>Home</a><a>Contact</a><a>About Us</a><a>Meet Our Specialists</a><a>Previous Sales</a><a>How to Buy</a><a>Next Sales</a></div>
  </div>
  <div class="social">
    <a style="background:#3b5998"><span class="sq"></span>Sharebook</a>
    <a style="background:#2aa3ef"><span class="sq"></span>Chirper</a>
    <a style="background:#d2442f"><span class="sq"></span>Circleplus</a>
  </div>
</footer>
</body>
</html>
```